Plate-on-Call Gift Coupon

About Us-
Plate-on-Call is a Tasmanian owned food delivery business which delivers meals from an increasing range of selected restaurants. We provide customers with quality food from reputed restaurants at reasonable delivery charges that meet the highest standards of quality and freshness.
We need some gift coupons/vouchers for our privileged customers. We need three designs which are as follows:
1) 10% OFF
2) FREE DELIVERY
3) FREE DELIVERY when you add any Wine/Beer
Coupons should have following:
Plate-on-Call Logo
Coupon Code: __________
Note:Redeem this coupon on www.plateoncall.com.au

```html
<!DOCTYPE html>
<html lang="en">
<head>
<meta charset="utf-8">
<title>Plate-on-Call Gift Coupon</title>
<link href="https://fonts.googleapis.com/css2?family=Roboto+Condensed:wght@700&family=Carlito:wght@400;700&family=Arimo:wght@400&display=swap" rel="stylesheet">
<style>
  :root {
    --orange: #f26a10;
    --orange-deep: #e85a00;
    --ink: #111111;
    --brand-grey: #3a3a3a;
    --navy: #0b1630;
    --blue: #3d6fb8;
    --paper: #ffffff;
    --peach: #fde2c6;
  }
  html, body { margin: 0; padding: 0; overflow: hidden; background: var(--paper); }
  .coupon {
    position: relative;
    width: 1200px;
    height: 720px;
    overflow: hidden;
    background: var(--paper);
  }
  .coupon-header {
    position: absolute; left: 0; top: 0; width: 1200px; height: 118px;
    background: var(--paper);
  }
  .brand-mark {
    position: absolute; left: 86px; top: 10px; width: 100px; height: 100px;
    border-radius: 22px; background: var(--orange);
  }
  .brand-name {
    position: absolute; left: 204px; top: 14px;
    font-family: "Roboto Condensed", sans-serif; font-weight: 700;
    font-size: 62px; line-height: 1; color: var(--brand-grey);
    letter-spacing: 0.5px;
  }
  .brand-tagline {
    position: absolute; left: 206px; top: 78px;
    font-family: "Arimo", sans-serif; font-size: 29px; line-height: 1;
    color: var(--orange);
  }
  .divider { position: absolute; left: 0; top: 116px; width: 1200px; height: 22px; }
  .coupon-body {
    position: absolute; left: 0; top: 136px; width: 1200px; height: 584px;
    background:
      radial-gradient(ellipse 900px 620px at 1180px 60px, var(--peach) 0%, rgba(253,226,198,0.55) 45%, rgba(255,255,255,0) 80%),
      var(--paper);
  }
  .offer {
    position: absolute; margin: 0;
    font-family: "Roboto Condensed", sans-serif; font-weight: 700; line-height: 1;
    white-space: nowrap;
  }
  .offer-discount { left: 48px; top: 210px; font-size: 70px; color: var(--orange); }
  .offer-delivery { left: 48px; top: 304px; font-size: 70px; color: var(--ink); }
  .offer-delivery .accent { color: var(--orange); }
  .offer-condition { left: 66px; top: 410px; font-size: 66px; color: var(--ink); letter-spacing: 0.3px; }
  .coupon-code {
    position: absolute; left: 60px; top: 556px;
    font-family: "Carlito", sans-serif; font-weight: 400; font-size: 74px; line-height: 1;
    color: var(--ink); white-space: nowrap;
  }
  .code-blank {
    display: inline-block; width: 400px; height: 5px; background: var(--ink);
    vertical-align: baseline; margin-left: 14px;
  }
  .redeem-note {
    position: absolute; left: 22px; right: 20px; top: 664px;
    display: flex; justify-content: space-between;
    font-family: "Arimo", sans-serif; font-size: 41px; line-height: 1; color: var(--ink);
  }
  .redeem-note .label { color: var(--orange-deep); }
</style>
</head>
<body>
<main class="coupon">
  <header class="coupon-header">
    <div class="brand-mark"></div>
    <div class="brand-name">Plate-on-Call</div>
    <div class="brand-tagline">you call we carry</div>
  </header>

  <div class="coupon-body" role="img" aria-label="Soft peach light rays radiating from the upper right"></div>

  <svg class="divider" viewBox="0 0 1200 22" preserveAspectRatio="none">
    <defs>
      <linearGradient id="band-glow" x1="0" y1="0" x2="0" y2="1">
        <stop offset="0" stop-color="var(--blue)" stop-opacity="0.9"/>
        <stop offset="1" stop-color="var(--blue)" stop-opacity="0"/>
      </linearGradient>
    </defs>
    <rect x="0" y="6" width="1200" height="14" fill="url(#band-glow)"/>
    <polygon points="0,2 1200,0 1200,9 0,8" fill="var(--navy)"/>
  </svg>

  <p class="offer offer-discount">10% OFF</p>
  <p class="offer offer-delivery"><span class="accent">FREE</span> DELIVERY</p>
  <p class="offer offer-condition">when you add any Wine/Beer</p>

  <div class="coupon-code">Coupon Code:<span class="code-blank"></span></div>

  <div class="redeem-note">
    <span><span class="label">Note:</span>Redeem</span>
    <span>this</span>
    <span>coupon</span>
    <span>on</span>
    <span>www.plateoncall.com</span>
  </div>
</main>
</body>
</html>
```